Eye Catching Wrap for Tidewell Plumbing

We would like a truck wrap (box truck/transit) that is distinguishable, unique, and eye catching. Stick with the basic colors within the logo but feel free to add more as long as it’s not over done. Must include the following:
-phone number (big and bold 555-827-3906)
-logo
-“Tidewell Quality Guaranteed” (or your own slogan if it’s better
-military and first responder discounts
-website

```html
<!DOCTYPE html>
<html lang="en">
<head>
<meta charset="utf-8">
<title>Tidewell Plumbing – Truck Wrap</title>
<link rel="stylesheet" href="https://fonts.googleapis.com/css2?family=Montserrat:wght@700;800&display=swap">
<style>
  :root {
    --wrap-blue: #1d5aa8;
    --wrap-orange: #f25a1c;
    --wrap-cyan: #22b3d6;
    --wrap-white: #ffffff;
    --backdrop: #e9e7e2;
    --frame: #b9bcc0;
  }
  html, body {
    margin: 0;
    padding: 0;
    width: 1200px;
    height: 1200px;
    overflow: hidden;
    background: var(--backdrop);
    font-family: "Montserrat", Arial, sans-serif;
  }
  .canvas {
    position: relative;
    width: 1200px;
    height: 1200px;
  }
  .panel {
    position: absolute;
    background: var(--wrap-white);
    overflow: hidden;
    outline: 6px solid var(--frame);
  }
  .panel-bands {
    position: absolute;
    inset: 0;
    width: 100%;
    height: 100%;
  }
  .side-panel {
    left: 40px;
    top: 70px;
    width: 1120px;
    height: 400px;
  }
  .rear-panel {
    left: 400px;
    top: 560px;
    width: 400px;
    height: 580px;
  }
  .brand-badge {
    position: absolute;
    border-radius: 50%;
    background: var(--wrap-white);
    display: flex;
    align-items: center;
    justify-content: center;
    text-align: center;
    color: var(--wrap-blue);
    font-weight: 800;
    line-height: 1.05;
    text-transform: uppercase;
    box-shadow: 0 0 0 8px var(--wrap-orange);
  }
  .side-panel .brand-badge {
    left: 100px;
    top: 55px;
    width: 290px;
    height: 290px;
    font-size: 40px;
  }
  .rear-panel .brand-badge {
    left: 105px;
    top: 195px;
    width: 190px;
    height: 190px;
    font-size: 26px;
    box-shadow: 0 0 0 6px var(--wrap-orange);
  }
  .slogan {
    position: absolute;
    margin: 0;
    font-weight: 800;
    text-align: center;
    line-height: 1.05;
    text-transform: uppercase;
  }
  .slogan .slogan-top { display: block; color: var(--wrap-blue); }
  .slogan .slogan-bottom { display: block; color: var(--wrap-orange); }
  .side-panel .slogan {
    left: 470px;
    top: 60px;
    width: 620px;
    font-size: 52px;
  }
  .rear-panel .slogan {
    left: 0;
    top: 40px;
    width: 100%;
    font-size: 34px;
  }
  .phone {
    position: absolute;
    margin: 0;
    color: var(--wrap-white);
    font-weight: 700;
    letter-spacing: 2px;
    text-align: center;
  }
  .side-panel .phone {
    left: 470px;
    top: 228px;
    width: 620px;
    font-size: 64px;
  }
  .rear-panel .phone {
    left: 0;
    top: 430px;
    width: 100%;
    font-size: 40px;
  }
  .website {
    position: absolute;
    margin: 0;
    color: var(--wrap-white);
    font-weight: 700;
    text-align: center;
    letter-spacing: 1px;
  }
  .side-panel .website {
    left: 470px;
    top: 306px;
    width: 620px;
    font-size: 28px;
  }
  .rear-panel .website {
    left: 0;
    top: 526px;
    width: 100%;
    font-size: 22px;
  }
  .discounts {
    position: absolute;
    margin: 0;
    right: 30px;
    bottom: 14px;
    color: var(--wrap-white);
    font-weight: 700;
    font-size: 22px;
    letter-spacing: 2px;
    text-transform: uppercase;
  }
</style>
</head>
<body>
<main class="canvas">

  <section class="panel side-panel" aria-label="Truck box side">
    <svg class="panel-bands" viewBox="0 0 1120 400" preserveAspectRatio="none" aria-hidden="true">
      <polygon points="0,190 1120,176 1120,190 0,204" fill="var(--wrap-cyan)"/>
      <polygon points="0,214 1120,200 1120,345 0,345" fill="var(--wrap-blue)"/>
      <rect x="0" y="345" width="1120" height="55" fill="var(--wrap-orange)"/>
    </svg>
    <div class="brand-badge">Tidewell<br>Plumbing</div>
    <h1 class="slogan"><span class="slogan-top">Tidewell Quality</span><span class="slogan-bottom">Guaranteed</span></h1>
    <p class="phone">555-827-3906</p>
    <p class="website">www.tidewellplumbing.com</p>
    <p class="discounts">Military and First Responder Discounts</p>
  </section>

  <section class="panel rear-panel" aria-label="Truck box rear">
    <svg class="panel-bands" viewBox="0 0 400 580" preserveAspectRatio="none" aria-hidden="true">
      <polygon points="0,290 400,278 400,292 0,304" fill="var(--wrap-cyan)"/>
      <polygon points="0,314 400,302 400,505 0,520" fill="var(--wrap-blue)"/>
      <polygon points="0,520 400,505 400,580 0,580" fill="var(--wrap-orange)"/>
    </svg>
    <h2 class="slogan"><span class="slogan-top">Tidewell Quality</span><span class="slogan-bottom">Guaranteed</span></h2>
    <div class="brand-badge">Tidewell<br>Plumbing</div>
    <p class="phone">555-827-3906</p>
    <p class="website">www.tidewellplumbing.com</p>
  </section>

</main>
</body>
</html>
```